Comprehensive and creative superhero design needed for our mortgage company

We are a mortgage company called Steadfast Mortgages, and we are looking for a mascot to help project our identity. Our goal is to create a mascot that can express an explosive yet professional image. More importantly, we want our mascot to be universal and welcoming to people of all backgrounds. Our target audience is new and upcoming homebuyers.

We're looking for a mascot similar to "El Vuelcón" from the old Brindle commercials. We would like to include some form of a mask, and we don't mind the buff yet short physique of the character to remain the same. However, his character build and wardrobe is completely up to your interpretation, we are open to new ideas. It is important to note that we work with homes and money. Our two main colours are purple and yellow, however we are open to trying different colours such as green or blue. We embrace the concept that less is more.

Our plan is to display the mascot on the many trucks that we own to be advertised around the area, and we would like to include him on various other forms of media as well (website, social media, etc.). It is important to remember that the design we choose will be blown up to a much larger size. The most important part of our mascot project is that we need him in several poses so that we can incorporate him into our designs effectively. We've attached a file with the poses we would like to see the character in. These poses can either be included in your initial design, or they can be made after your design if it has been chosen. We also attached a file of "El Vuelcón," and we included the potential design of our truck for inspiration.

Note: The design must be different enough to avoid any copyright issues with the "El Vuelcón" design from Brindle

We look forward to seeing your designs! :)

```html
<!DOCTYPE html>
<html lang="en">
<head>
<meta charset="utf-8">
<title>Steadfast Mortgages – Trailer Wrap Panels</title>
<link rel="stylesheet" href="https://fonts.googleapis.com/css2?family=Anton&family=Bangers&display=swap">
<style>
  :root {
    --purple: #93368f;
    --purple-deep: #6e2370;
    --yellow: #fccb05;
    --gold: #e0a81c;
    --white: #ffffff;
    --frame: #1a1a1a;
    --page: #ffffff;
  }
  html, body {
    margin: 0;
    padding: 0;
    width: 1200px;
    height: 583px;
    overflow: hidden;
    background: var(--page);
  }
  .sheet {
    position: relative;
    width: 1200px;
    height: 583px;
  }
  .panel {
    position: absolute;
    display: block;
    border: 3px solid var(--frame);
    box-sizing: border-box;
    background: var(--purple);
  }
  .panel--side-a { left: 40px;  top: 45px;  width: 860px; height: 218px; }
  .panel--rear-a { left: 950px; top: 45px;  width: 200px; height: 218px; }
  .panel--side-b { left: 40px;  top: 318px; width: 860px; height: 218px; }
  .panel--rear-b { left: 950px; top: 318px; width: 200px; height: 218px; }
  .panel svg { display: block; width: 100%; height: 100%; }
  .burst { fill: var(--yellow); }
  .mascot-slot { fill: url(#mascotTone); }
  .brand-name {
    font-family: "Anton", "Impact", sans-serif;
    fill: var(--white);
  }
  .tagline {
    font-family: "Bangers", "Impact", sans-serif;
    fill: var(--purple);
    letter-spacing: 1px;
  }
</style>
</head>
<body>
<main class="sheet">

  <svg width="0" height="0" style="position:absolute" aria-hidden="true">
    <defs>
      <polygon id="burst" points="1,0 .657,.176 .866,.5 .481,.481 .5,.866 .176,.657 0,1 -.176,.657 -.5,.866 -.481,.481 -.866,.5 -.657,.176 -1,0 -.657,-.176 -.866,-.5 -.481,-.481 -.5,-.866 -.176,-.657 0,-1 .176,-.657 .5,-.866 .481,-.481 .866,-.5 .657,-.176"/>
      <linearGradient id="mascotTone" x1="0" y1="0" x2="0" y2="1">
        <stop offset="0" stop-color="#e8b84a"/>
        <stop offset=".5" stop-color="#c98fc4"/>
        <stop offset="1" stop-color="#f2c21a"/>
      </linearGradient>
    </defs>
  </svg>

  <!-- Side panel, version A -->
  <section class="panel panel--side-a">
    <svg viewBox="0 0 854 212" preserveAspectRatio="none">
      <use href="#burst" class="burst" transform="translate(525 106) scale(255 150)"/>
      <rect class="mascot-slot" x="120" y="6" width="118" height="200" rx="40" role="img" aria-label="Superhero mascot in purple suit and gold cape, arms crossed"/>
      <text class="brand-name" x="352" y="108" font-size="15">www.</text>
      <text class="brand-name" x="392" y="108" font-size="64">Steadfast</text>
      <text class="brand-name" x="345" y="160" font-size="54">Mortgages.ca</text>
      <text class="tagline" x="520" y="192" font-size="24" text-anchor="middle">WE CAN HELP</text>
    </svg>
  </section>

  <!-- Rear panel, version A -->
  <section class="panel panel--rear-a">
    <svg viewBox="0 0 194 212" preserveAspectRatio="none">
      <use href="#burst" class="burst" transform="translate(150 28) scale(80 48)"/>
      <text class="tagline" x="142" y="22" font-size="7.5" text-anchor="middle">MORTGAGES AREN'T EASY.</text>
      <text class="tagline" x="142" y="34" font-size="9" text-anchor="middle">WE'RE HERE TO HELP</text>
      <rect class="mascot-slot" x="14" y="28" width="100" height="118" rx="30" role="img" aria-label="Superhero mascot flying upward with thumbs up"/>
      <text class="brand-name" x="16" y="170" font-size="7">www.</text>
      <text class="brand-name" x="36" y="170" font-size="28">Steadfast</text>
      <text class="brand-name" x="16" y="198" font-size="24">Mortgages.ca</text>
    </svg>
  </section>

  <!-- Side panel, version B -->
  <section class="panel panel--side-b">
    <svg viewBox="0 0 854 212" preserveAspectRatio="none">
      <text class="brand-name" x="40" y="72" font-size="16">www.</text>
      <text class="brand-name" x="86" y="98" font-size="80">Steadfast</text>
      <text class="brand-name" x="40" y="170" font-size="66">Mortgages.ca</text>
      <use href="#burst" class="burst" transform="translate(640 106) scale(130 100)"/>
      <text class="tagline" x="640" y="100" font-size="32" text-anchor="middle">WE CAN</text>
      <text class="tagline" x="640" y="140" font-size="44" text-anchor="middle">HELP</text>
    </svg>
  </section>

  <!-- Rear panel, version B -->
  <section class="panel panel--rear-b">
    <svg viewBox="0 0 194 212" preserveAspectRatio="none">
      <rect class="mascot-slot" x="58" y="10" width="80" height="120" rx="28" role="img" aria-label="Superhero mascot standing with thumbs up"/>
      <text class="brand-name" x="16" y="166" font-size="7">www.</text>
      <text class="brand-name" x="36" y="166" font-size="28">Steadfast</text>
      <text class="brand-name" x="16" y="194" font-size="24">Mortgages.ca</text>
    </svg>
  </section>

</main>
</body>
</html>
```